Hair extensions packaging design

Professional hair extensions packaging design.
We like a clean and crisp look. The design should convey luxury and highest quality.

Target Market(s)

women ages 16-40

Industry/Entity Type

beauty, hair

Font styles to use
Other font styles liked:
• kiona

Requirements
Must have
• clean, crisp, professional look

```html
<!DOCTYPE html>
<html lang="en">
<head>
<meta charset="utf-8">
<title>Velmora Hair Extensions – Packaging Cards</title>
<link rel="stylesheet" href="https://fonts.googleapis.com/css2?family=Josefin+Sans:wght@300;400;600&family=Quicksand:wght@300;400&display=swap">
<style>
  :root {
    --paper: #ffffff;
    --card: #fdfdfd;
    --card-edge: #ececec;
    --gold: #b8893a;
    --gold-soft: #c9a266;
    --hair-dark: #a8773f;
    --hair-mid: #c99b62;
    --hair-light: #dfc094;
  }
  * { margin: 0; padding: 0; box-sizing: border-box; }
  html, body { width: 1200px; height: 577px; overflow: hidden; background: var(--paper); }
  .canvas { position: relative; width: 1200px; height: 577px; overflow: hidden; }

  .hair-bundle {
    position: absolute; top: 271px; height: 306px;
    background: linear-gradient(90deg, rgba(255,255,255,0) 0%, var(--hair-dark) 8%, var(--hair-mid) 30%, var(--hair-light) 50%, var(--hair-mid) 72%, var(--hair-light) 88%, rgba(255,255,255,0) 100%);
  }
  .hair-bundle--front { left: 94px; width: 426px; }
  .hair-bundle--back { left: 680px; width: 420px; }

  .card {
    position: absolute; top: 7px; width: 403px; height: 263px;
    background: var(--card); border: 1px solid var(--card-edge);
    color: var(--gold);
  }
  .card::before {
    content: ""; position: absolute; left: -15px; top: 0; bottom: -1px; width: 15px;
    border-bottom: 1px solid var(--card-edge);
    background: linear-gradient(to bottom right, transparent 49.6%, var(--card-edge) 50%, transparent 50.4%);
  }
  .card--front { left: 115px; text-align: center; }
  .card--back { left: 700px; top: 6px; }

  .brand-mark {
    position: absolute; top: 76px; left: 0; right: 0;
    display: flex; justify-content: center; align-items: center; gap: 8px;
    font-family: "Josefin Sans", sans-serif; font-weight: 300;
    font-size: 15px; letter-spacing: 1px; color: var(--gold);
  }
  .brand-mark__square { width: 9px; height: 9px; border: 1px solid var(--gold); }

  .headline {
    position: absolute; top: 152px; left: 0; right: 0;
    font-family: "Josefin Sans", sans-serif; font-weight: 400;
    font-size: 10.5px; letter-spacing: 1.1px; text-transform: uppercase;
  }
  .quality-strip {
    position: absolute; top: 164px; left: 71px; width: 261px; height: 16px;
    border: 1px solid var(--gold-soft);
    font-family: "Josefin Sans", sans-serif; font-size: 7.6px; letter-spacing: .7px;
    line-height: 15px; text-transform: uppercase;
  }
  .donor-note {
    position: absolute; top: 222px; left: 0; right: 0;
    font-family: "Josefin Sans", sans-serif; font-size: 6.5px; letter-spacing: .5px;
    line-height: 9px; text-transform: uppercase;
  }
  .site-url {
    position: absolute; top: 247px; left: 0; right: 0;
    font-family: "Josefin Sans", sans-serif; font-size: 6.5px; letter-spacing: .6px;
    text-transform: uppercase;
  }

  .care { position: absolute; top: 82px; left: 38px; width: 340px; }
  .care__title {
    font-family: "Josefin Sans", sans-serif; font-weight: 600;
    font-size: 11.5px; letter-spacing: .3px; text-transform: uppercase; line-height: 13px;
    margin-bottom: 0;
  }
  .care__list { list-style: none; }
  .care__list li, .care__about {
    font-family: "Quicksand", sans-serif; font-weight: 300;
    font-size: 10.4px; line-height: 12px;
  }
  .care__list li { padding-left: 7px; text-indent: -7px; }
  .care__about { margin-top: 12px; }
</style>
</head>
<body>
<div class="canvas">
  <div class="hair-bundle hair-bundle--front" role="img" aria-label="Photo of straight blonde and honey-brown human hair extension bundle"></div>
  <div class="hair-bundle hair-bundle--back" role="img" aria-label="Photo of straight blonde and honey-brown human hair extension bundle"></div>

  <section class="card card--front">
    <div class="brand-mark"><span class="brand-mark__square"></span><span>VELMORA</span></div>
    <p class="headline">We guarentee the highest quality of our products</p>
    <p class="quality-strip">Highest quality &nbsp;|&nbsp; Double drawn &nbsp;|&nbsp; 100% human remi hair</p>
    <p class="donor-note">Velmora hair is cut directly from the donor<br>to ensure the cuticle remains in tact and the hair will never tangle!</p>
    <p class="site-url">www.velmorahair.com</p>
  </section>

  <section class="card card--back">
    <div class="care">
      <h2 class="care__title">Care instructions</h2>
      <ul class="care__list">
        <li>-Velmora provides only the highest in quality, human remi hair &nbsp;that requires very little care to maintain its luxurious feel</li>
        <li>-Wash the hair with a sulfate free shampoo and follow with a moisturizing conditioner that is formulated for hair extensions</li>
      </ul>
      <p class="care__about">We proudly show our immense passion for delivering superior quality in our full product line. Velmora is strongly committed to serving their clients with utmost integrity, believing in a foundation of personal and professional ethics and our over 25 years of service in the beauty industry!</p>
    </div>
  </section>
</div>
</body>
</html>
```